Web Page Design for a Website that Provides Tutoring

I am looking to create an online tutoring website. The website will allow parents or students to contact tutors with a view to instructing them to tutor themselves or their children.

The name of the website is LendYourLessons.

This brief is to create the design for one of the web pages for this web site. I am hoping the same designer will be available to design other pages.

The page I want designed is one of the more complex and I have attached the design as an excel spreadsheet. The web page needs to include all the items on this page but if you want to change the positioning of the items then Im fine with that.

I recently had two logos created for this website. My favourite is the one with a mortar board but im not sure I like the colours. I have attached both of these logos and you can use either of them, change the colours or create something different. I just want a design pleasing to the eye. If the logo is changed I would like that in a seperate file.

So can you please submit designs for this page. I have attached the two logos which you can use, change or if you feel you have a better idea then you can use that.

On the spreadsheet the Send Message, Favourite etc are buttons.

Target Market(s)

People who want to better themselves.
Possible middle class to upper class.

Industry/Entity Type

Tutoring

Number of Pages Required

1 page

Requirements
Must have
• The designs must have alot of the information attached in the spreadsheet.

```html
<!DOCTYPE html>
<html lang="en">
<head>
<meta charset="utf-8">
<title>LendYourLessons – Tutor Profile</title>
<link href="https://fonts.googleapis.com/css2?family=Open+Sans:wght@400;600;700&family=Roboto+Slab:wght@300;400;700&display=swap" rel="stylesheet">
<style>
:root{
  --orange:#f26543;
  --blue:#355d9a;
  --blue-dark:#2d5189;
  --ink:#333740;
  --muted:#8a8f98;
  --line:#e3e5e8;
  --paper:#ffffff;
  --mist:#f3f3f4;
  --board:#3c3d3f;
  --board-2:#565759;
  --yellow:#f7b626;
  --sky:#1e9ad6;
  --red:#e8463f;
  --teal:#129181;
  --head-font:'Roboto Slab',Georgia,serif;
  --body-font:'Open Sans',Arial,sans-serif;
}
*{box-sizing:border-box;margin:0;padding:0}
html,body{width:1200px;height:3704px;overflow:hidden}
body{position:relative;background:var(--paper);font-family:var(--body-font);color:var(--ink)}
.abs{position:absolute}
a{color:inherit;text-decoration:none}

/* header */
.site-header{position:absolute;left:0;top:0;width:1200px;height:94px;background:#fff}
.brand{position:absolute;left:153px;top:28px;display:flex;align-items:center;gap:10px}
.brand-mark{width:34px;height:34px;background:var(--blue);border-radius:4px}
.brand-name{font-family:var(--body-font);font-weight:700;font-size:21px;color:var(--blue)}
.main-nav{position:absolute;left:400px;top:38px;display:flex;gap:0;font-size:16px;font-weight:600}
.main-nav a{display:block;padding:0 24px;line-height:36px;height:36px;margin-right:16px}
.main-nav a.active{border:2px solid var(--orange);border-radius:18px;color:var(--orange);width:100px;text-align:center;margin-right:34px}
.header-tools{position:absolute;left:960px;top:38px;display:flex;gap:16px}
.tool-btn{width:34px;height:34px;border-radius:50%;display:flex;align-items:center;justify-content:center}
.tool-btn.search{background:var(--blue)}
.tool-btn.user{background:var(--orange)}

/* hero */
.hero{position:absolute;left:0;top:94px;width:1200px;height:499px;background:radial-gradient(ellipse at 55% 40%,var(--board-2),var(--board) 70%)}
.hero-photo{position:absolute;left:180px;top:49px;width:306px;height:306px;border-radius:50%;border:5px solid #fff;background:linear-gradient(160deg,#c9ccd2,#7d8490 60%,#4b5260)}
.slider-arrow{position:absolute;width:36px;height:36px;border-radius:50%;background:#fff;display:flex;align-items:center;justify-content:center}
.hero .slider-arrow{top:184px}
.hero-copy{position:absolute;left:536px;top:70px;width:560px;color:#fff}
.hero-tag{display:inline-block;background:var(--orange);font-size:15px;font-weight:600;padding:6px 34px 6px 14px;clip-path:polygon(0 0,100% 0,88% 100%,0 100%)}
.hero-name{font-family:var(--head-font);font-weight:400;font-size:40px;margin-top:12px;line-height:1}
.hero-degree{font-size:15px;line-height:22px;margin-top:8px;width:380px}
.hero-rule{width:140px;height:2px;background:rgba(255,255,255,.6);margin:14px 0 28px}
.hero-bio{font-size:14px;line-height:21px;color:#e4e4e4}
.explore{display:flex;align-items:center;gap:8px;font-size:15px;font-weight:600;margin-top:38px}

.action-panel{position:absolute;left:156px;top:496px;width:889px;height:198px;background:var(--blue);display:flex;box-shadow:0 8px 20px rgba(0,0,0,.2)}
.action-col{flex:1;text-align:center;color:#fff;padding-top:38px;position:relative}
.action-col+.action-col::before{content:"";position:absolute;left:0;top:30px;bottom:30px;border-left:1px solid rgba(255,255,255,.3)}
.action-title{font-size:24px;line-height:28px}
.action-sub{font-size:14px;margin-top:2px}
.stars{display:flex;justify-content:center;gap:4px}
.pill{display:inline-flex;align-items:center;gap:8px;height:34px;padding:0 26px;border-radius:17px;border:2px solid #fff;font-size:14px;font-weight:600;margin-top:22px;color:#fff}
.pill.solid{background:var(--orange);border-color:var(--orange)}

/* welcome */
.welcome{position:absolute;left:0;top:770px;width:1200px;text-align:center}
.welcome-mark{width:40px;height:40px;background:var(--blue);border-radius:4px;margin:0 auto}
.welcome h1{font-family:var(--head-font);font-weight:400;font-size:32px;margin-top:12px}
.welcome h1 span{color:var(--blue)}
.welcome-rule{width:70px;height:2px;background:var(--line);margin:10px auto 14px}
.welcome p{width:740px;margin:0 auto;font-size:13px;line-height:20px;color:var(--muted)}
.discover{display:inline-flex;align-items:center;gap:8px;margin-top:48px;font-size:14px;font-weight:600;color:var(--blue)}

/* find tutor */
.finder-band{position:absolute;left:0;top:1144px;width:1200px;height:284px;background:linear-gradient(90deg,#d7d8da,#eeeeec 40%,#c9c2ba 55%,#dedfe1 75%,#cfd1d3)}
.finder-person{position:absolute;left:620px;top:1078px;width:250px;height:350px;background:linear-gradient(180deg,#e8c7a8,#b88c6d 50%,#8f5a48);border-radius:120px 120px 0 0}
.finder{position:absolute;left:232px;top:1077px;width:356px;height:415px;background:var(--orange);padding:40px 32px;color:#fff}
.finder h2{font-family:var(--head-font);font-weight:400;font-size:28px;padding-left:20px}
.finder-rule{width:150px;height:1px;background:rgba(255,255,255,.6);margin:6px 0 24px 20px}
.select{height:34px;background:#fff;border-radius:3px;margin:0 0 16px 0;display:flex;align-items:center;justify-content:space-between;padding:0 12px;font-size:12px;color:var(--muted);width:292px}
.finder .pill{margin-top:8px;height:32px;padding:0 28px}

/* pricing */
.section-title{position:absolute;left:0;width:1200px;text-align:center;font-family:var(--head-font);font-size:28px;font-weight:400}
.price-table{position:absolute;left:156px;top:1620px;width:889px;border-collapse:collapse;box-shadow:0 6px 18px rgba(0,0,0,.12);font-size:14px;text-align:center}
.price-table th{height:79px;color:#fff;font-weight:600;background:var(--blue);width:12.7%}
.price-table th:nth-child(even){background:var(--blue-dark)}
.price-table th:first-child{width:20%}
.price-table td{height:50px;border-top:1px solid var(--line);color:#666;background:#fff}
.price-table td+td{border-left:1px solid var(--line)}

/* reviews */
.reviews{position:absolute;left:0;top:1865px;width:1200px;height:655px;background:var(--mist)}
.reviews .slider-arrow{top:376px;background:#bdbec1}
.reviews .slider-arrow.next{background:var(--orange)}
.review{position:absolute;top:140px;width:360px;text-align:center}
.review-photo{width:172px;height:172px;border-radius:50%;margin:0 auto;border:4px solid #fff;background:linear-gradient(160deg,#d9dbe0,#8b9099 60%,#555b66)}
.review-name{display:flex;justify-content:center;align-items:center;gap:10px;margin-top:22px;font-family:var(--head-font);font-size:20px;color:var(--blue)}
.review-date{font-size:12px;color:var(--muted);margin-top:6px;display:flex;justify-content:center;gap:6px;align-items:center}
.review-rule{height:1px;background:#d5d7da;margin:14px 0 0;position:relative}
.review-rule::after{content:"";position:absolute;left:172px;top:0;border:8px solid transparent;border-top-color:#d5d7da}
.review h4{font-size:15px;font-weight:700;margin-top:24px}
.review blockquote{font-size:13px;line-height:19px;color:#666;margin-top:8px}
.review-icon{margin:16px auto 0;width:28px}
.review-author{font-size:14px;margin-top:2px}
.review-role{font-size:12px;color:#666}

/* calendar */
.calendar{position:absolute;left:232px;top:2650px;width:736px;height:528px;background:#f6f6f6}
.cal-head{height:55px;background:var(--orange);color:#fff;display:flex;justify-content:center;align-items:center;gap:90px;font-size:18px;font-weight:600}
.cal-grid{position:absolute;left:28px;top:80px;width:680px;display:grid;grid-template-columns:90px repeat(7,1fr);font-size:13px;color:#555}
.cal-grid div{height:57px;border-bottom:1px solid #e2e2e2;padding:12px 10px;position:relative}
.cal-grid .label{height:34px;border-bottom:1px solid #d8d8d8;font-weight:700;padding:4px 10px}
.cal-grid .label.timing{color:var(--blue)}
.cal-grid .dim{color:#b6b6b6}
.cal-grid .open{background:#fff}
.cal-grid .time{color:var(--blue)}
.bar::after{content:"";position:absolute;left:0;right:0;bottom:-1px;height:4px}
.bar.y::after{background:var(--yellow)}.bar.b::after{background:var(--sky)}.bar.r::after{background:var(--red)}.bar.t::after{background:var(--teal)}
.legend{position:absolute;left:0;top:422px;width:100%;display:flex;justify-content:center;gap:34px;font-size:13px}
.legend span{display:flex;align-items:center;gap:8px}
.legend i{width:12px;height:12px;display:block}
.cal-foot{position:absolute;left:0;bottom:0;width:100%;height:56px;background:#8e8e90;color:#fff;text-align:center;line-height:56px;font-size:14px;font-weight:600}

/* footer */
.site-footer{position:absolute;left:0;top:3344px;width:1200px;height:360px;background:radial-gradient(ellipse at 50% 40%,var(--board-2),var(--board) 70%)}
.cta{position:absolute;left:156px;top:3243px;width:889px;height:195px;background:var(--blue);text-align:center;color:#fff;padding-top:38px}
.cta h3{font-family:var(--head-font);font-weight:400;font-size:28px;line-height:36px}
.cta .pill{margin-top:20px;height:34px;padding:0 34px}
.socials{position:absolute;left:0;top:3522px;width:1200px;display:flex;justify-content:center;gap:12px}
.socials i{width:36px;height:36px;border-radius:50%;background:#d8d8d8;display:block}
.copyright{position:absolute;left:0;top:3586px;width:1200px;text-align:center;color:#e6e6e6;font-size:13px;line-height:22px}
.to-top{position:absolute;left:1114px;top:3569px;width:40px;height:40px;border-radius:50%;background:var(--orange);display:flex;align-items:center;justify-content:center}
</style>
</head>
<body>

<header class="site-header">
  <div class="brand"><span class="brand-mark"></span><span class="brand-name">LendYourLessons</span></div>
  <nav class="main-nav">
    <a class="active" href="#">Home</a><a href="#">About</a><a href="#">Student</a><a href="#">Tutor</a><a href="#">Contact</a>
  </nav>
  <div class="header-tools">
    <span class="tool-btn search"><svg width="16" height="16" viewBox="0 0 16 16"><circle cx="7" cy="7" r="4.5" fill="none" stroke="#fff" stroke-width="2"/><path d="M10.5 10.5L14 14" stroke="#fff" stroke-width="2"/></svg></span>
    <span class="tool-btn user"><svg width="16" height="16" viewBox="0 0 16 16"><circle cx="8" cy="5.5" r="3" fill="none" stroke="#fff" stroke-width="1.8"/><path d="M3 14c0-3 2.2-4.5 5-4.5s5 1.5 5 4.5z" fill="none" stroke="#fff" stroke-width="1.8"/></svg></span>
  </div>
</header>

<section class="hero">
  <div class="hero-photo" role="img" aria-label="Portrait photo of the tutor"></div>
  <span class="slider-arrow" style="left:96px"><svg width="12" height="12" viewBox="0 0 12 12"><path d="M8 1L3 6l5 5" fill="none" stroke="#333" stroke-width="2"/></svg></span>
  <span class="slider-arrow" style="left:1066px"><svg width="12" height="12" viewBox="0 0 12 12"><path d="M4 1l5 5-5 5" fill="none" stroke="#333" stroke-width="2"/></svg></span>
  <div class="hero-copy">
    <span class="hero-tag">Hi, I am</span>
    <h2 class="hero-name">Martin Fielding</h2>
    <p class="hero-degree">First Class Honours in Economics from Ashdown University.</p>
    <div class="hero-rule"></div>
    <p class="hero-bio">Three years part time experience in teaching Mathematics and Economics. Specialises in teaching Mathematics / Economics / Bussiness Studies for A-Level / GCSE/IB</p>
    <a class="explore" href="#"><svg width="14" height="14" viewBox="0 0 14 14"><circle cx="7" cy="7" r="7" fill="#fff"/><path d="M5.5 4l3 3-3 3" fill="none" stroke="#3c3d3f" stroke-width="1.6"/></svg>Explore More ...</a>
  </div>
</section>

<section class="action-panel">
  <div class="action-col">
    <div class="stars">
      <svg width="170" height="30" viewBox="0 0 170 30">
        <defs><path id="st" d="M15 1l4.2 9 9.8 1.1-7.3 6.6 2 9.7L15 22.5 6.3 27.4l2-9.7L1 11.1l9.8-1.1z"/>
        <clipPath id="half"><rect x="0" y="0" width="15" height="30"/></clipPath></defs>
        <use href="#st" fill="var(--yellow)"/><use href="#st" x="35" fill="var(--yellow)"/><use href="#st" x="70" fill="var(--yellow)"/>
        <use href="#st" x="105" fill="none" stroke="var(--yellow)" stroke-width="2"/><g transform="translate(105 0)"><use href="#st" fill="var(--yellow)" clip-path="url(#half)"/></g>
        <use href="#st" x="140" fill="none" stroke="var(--yellow)" stroke-width="2"/>
      </svg>
    </div>
    <div class="action-sub" style="margin-top:8px">Over All Review</div>
    <a class="pill solid" href="#"><svg width="12" height="12" viewBox="0 0 12 12"><path d="M1 11l1-3 6-6 2 2-6 6z" fill="#fff"/></svg>Write Review</a>
  </div>
  <div class="action-col">
    <div class="action-title">For Questions,</div>
    <div class="action-sub">Queries and Help?</div>
    <a class="pill" href="#"><svg width="13" height="13" viewBox="0 0 13 13"><path d="M1 6l11-5-4 11-2-4z" fill="#fff"/></svg>Send Message</a>
  </div>
  <div class="action-col">
    <div class="action-title">We Welcome</div>
    <div class="action-sub">Your Suggestions</div>
    <a class="pill" href="#"><svg width="13" height="13" viewBox="0 0 13 13"><circle cx="6.5" cy="4" r="2.5" fill="none" stroke="#fff" stroke-width="1.5"/><path d="M2 12c0-3 2-4.5 4.5-4.5S11 9 11 12z" fill="none" stroke="#fff" stroke-width="1.5"/></svg>Favour Tutor</a>
  </div>
</section>

<section class="welcome">
  <div class="welcome-mark"></div>
  <h1>Welcome to <span>LendYourLessons</span></h1>
  <div class="welcome-rule"></div>
  <p>Lorem Ipsum is simply dummy text of the printing and typesetting industry. Lorem Ipsum has been the industry's standard dummy text ever since the 1500s, when an unknown printer took a galley of type and scrambled it to make a type specimen book. It has survived not only five centuries, but also the leap into electronic typesetting, remaining essentially unchanged.</p>
  <a class="discover" href="#"><svg width="14" height="14" viewBox="0 0 14 14"><circle cx="7" cy="7" r="7" fill="var(--blue)"/><path d="M5.5 4l3 3-3 3" fill="none" stroke="#fff" stroke-width="1.6"/></svg>Discover More About Us ...</a>
</section>

<div class="finder-band" role="img" aria-label="Blurred classroom photo"></div>
<div class="finder-person" role="img" aria-label="Photo of a smiling tutor holding a book"></div>
<section class="finder">
  <h2>Find Your Tutor</h2>
  <div class="finder-rule"></div>
  <div class="select">Tutoring type<svg width="10" height="6" viewBox="0 0 10 6"><path d="M1 1l4 4 4-4" fill="none" stroke="#999" stroke-width="1.4"/></svg></div>
  <div class="select">Willing to travel<svg width="10" height="6" viewBox="0 0 10 6"><path d="M1 1l4 4 4-4" fill="none" stroke="#999" stroke-width="1.4"/></svg></div>
  <div class="select">Select your age<svg width="10" height="6" viewBox="0 0 10 6"><path d="M1 1l4 4 4-4" fill="none" stroke="#999" stroke-width="1.4"/></svg></div>
  <div class="select">DBS (CRB)<svg width="10" height="6" viewBox="0 0 10 6"><path d="M1 1l4 4 4-4" fill="none" stroke="#999" stroke-width="1.4"/></svg></div>
  <a class="pill" href="#"><svg width="13" height="13" viewBox="0 0 16 16"><circle cx="7" cy="7" r="4.5" fill="none" stroke="#fff" stroke-width="2"/><path d="M10.5 10.5L14 14" stroke="#fff" stroke-width="2"/></svg>Search</a>
</section>

<h2 class="section-title" style="top:1548px">Pricing Table</h2>
<table class="price-table">
  <tr><th>Subjects<br>We Taught</th><th>Primary</th><th>Secondary</th><th>GCSE</th><th>A-Level</th><th>University</th><th>Adult<br>Learner</th></tr>
  <tr><td>Biology</td><td>£20</td><td>£20</td><td>£20</td><td>£20</td><td>£20</td><td>£20</td></tr>
  <tr><td>Chemistry</td><td>£20</td><td>£20</td><td>£20</td><td>£20</td><td>£20</td><td>£20</td></tr>
</table>

<section class="reviews">
  <h2 class="section-title" style="top:54px">Tutor's&nbsp; Reviews</h2>
  <span class="slider-arrow" style="left:96px"><svg width="12" height="12" viewBox="0 0 12 12"><path d="M8 1L3 6l5 5" fill="none" stroke="#fff" stroke-width="2"/></svg></span>
  <span class="slider-arrow next" style="left:1066px"><svg width="12" height="12" viewBox="0 0 12 12"><path d="M4 1l5 5-5 5" fill="none" stroke="#fff" stroke-width="2"/></svg></span>

  <article class="review" style="left:230px">
    <div class="review-photo" role="img" aria-label="Portrait photo of a tutor"></div>
    <div class="review-name">Joan Pearce <span style="color:#999">/</span>
      <svg width="90" height="16" viewBox="0 0 170 30"><use href="#st" fill="var(--yellow)"/><use href="#st" x="35" fill="var(--yellow)"/><use href="#st" x="70" fill="var(--yellow)"/><g transform="translate(105 0)"><use href="#st" fill="var(--yellow)" clip-path="url(#half)"/></g><use href="#st" x="105" fill="none" stroke="var(--yellow)" stroke-width="2"/><use href="#st" x="140" fill="none" stroke="var(--yellow)" stroke-width="2"/></svg></div>
    <div class="review-date"><svg width="11" height="11" viewBox="0 0 11 11"><rect x="1" y="2" width="9" height="8" fill="none" stroke="#888"/><path d="M1 4.5h9" stroke="#888"/></svg>SUNDAY, JUNE 26, 2016</div>
    <div class="review-rule"></div>
    <h4>Tutees&nbsp; Feedback</h4>
    <blockquote>"I never thought finance and accounting could be so interesting. I now enjoy challenging questions. I admire her passion and dedication to teaching."</blockquote>
    <svg class="review-icon" width="28" height="26" viewBox="0 0 28 26"><path d="M3 3h17v12H9l-5 4v-4H3z" fill="none" stroke="var(--blue)" stroke-width="2"/><circle cx="20" cy="18" r="6" fill="#fff" stroke="var(--blue)" stroke-width="2"/></svg>
    <div class="review-author">Kirsten Sallow</div>
    <div class="review-role">(Student)</div>
  </article>

  <article class="review" style="left:610px">
    <div class="review-photo" role="img" aria-label="Portrait photo of a tutor"></div>
    <div class="review-name">Colm Ashby <span style="color:#999">/</span>
      <svg width="90" height="16" viewBox="0 0 170 30"><use href="#st" fill="var(--yellow)"/><use href="#st" x="35" fill="var(--yellow)"/><use href="#st" x="70" fill="var(--yellow)"/><g transform="translate(105 0)"><use href="#st" fill="var(--yellow)" clip-path="url(#half)"/></g><use href="#st" x="105" fill="none" stroke="var(--yellow)" stroke-width="2"/><use href="#st" x="140" fill="none" stroke="var(--yellow)" stroke-width="2"/></svg></div>
    <div class="review-date"><svg width="11" height="11" viewBox="0 0 11 11"><rect x="1" y="2" width="9" height="8" fill="none" stroke="#888"/><path d="M1 4.5h9" stroke="#888"/></svg>SUNDAY, JUNE 26, 2016</div>
    <div class="review-rule"></div>
    <h4>Tutees&nbsp; Feedback</h4>
    <blockquote>"I never thought finance and accounting could be so interesting. I now enjoy challenging questions. I admire her passion and dedication to teaching."</blockquote>
    <svg class="review-icon" width="28" height="26" viewBox="0 0 28 26"><path d="M3 3h17v12H9l-5 4v-4H3z" fill="none" stroke="var(--blue)" stroke-width="2"/><circle cx="20" cy="18" r="6" fill="#fff" stroke="var(--blue)" stroke-width="2"/></svg>
    <div class="review-author">Reginald</div>
    <div class="review-role">(Parent)</div>
  </article>
</section>

<h2 class="section-title" style="top:2578px">December 2016</h2>
<section class="calendar">
  <div class="cal-head"><span>‹</span><span>December</span><span>›</span></div>
  <div class="cal-grid">
    <div class="label timing">TIMING</div><div class="label">MON</div><div class="label">TUE</div><div class="label">WED</div><div class="label">THU</div><div class="label">FRI</div><div class="label">SAT</div><div class="label">SUN</div>
    <div class="time">◷ 7-8</div><div class="dim">28</div><div class="dim">29</div><div class="dim">30</div><div>1</div><div>2</div><div class="open bar t">3</div><div>4</div>
    <div class="time">◷ 8-9</div><div>5</div><div>6</div><div class="open bar b">7</div><div>8</div><div>9</div><div>10</div><div>11</div>
    <div class="time">◷ 4-5</div><div>12</div><div>13</div><div class="open bar r">14</div><div class="open bar y">15</div><div>16</div><div>17</div><div>18</div>
    <div class="time">◷ 5-6</div><div>19</div><div>20</div><div>21</div><div>22</div><div>23</div><div>24</div><div>25</div>
    <div class="time">◷ 7-8</div><div class="open bar y">26</div><div class="bar y">27</div><div class="open bar t">28</div><div class="open bar r">29</div><div class="open">30</div><div>31</div><div class="dim">1</div>
  </div>
  <div class="legend">
    <span><i style="background:var(--yellow)"></i>Available</span>
    <span><i style="background:var(--sky)"></i>Taken</span>
    <span><i style="background:var(--red)"></i>Reserved</span>
    <span><i style="background:var(--teal)"></i>No</span>
  </div>
  <div class="cal-foot">January</div>
</section>

<footer class="site-footer"></footer>
<section class="cta">
  <h3>Get the Best Tutors - Live | Online | @Home<br>Anytime Anywhere</h3>
  <a class="pill" href="#">Join Now</a>
</section>
<div class="socials" aria-label="Social links"><i></i><i style="background:var(--orange)"></i><i></i><i></i></div>
<p class="copyright">© 2016 LendYourLessons.<br><span style="font-size:11px">All Rights Reserved.</span></p>
<span class="to-top"><svg width="14" height="10" viewBox="0 0 14 10"><path d="M1 8l6-6 6 6" fill="none" stroke="#fff" stroke-width="2"/></svg></span>

</body>
</html>
```